Sickle Cell Patient Flyer

I need this be appealing to families dealing with sickle cell disease. Both informative-introducing the idea that a stroke prevention program is not only easy for their children but necessary. Stroke is a risk to all with children with SCD.
I included a few info flyers from the Brainward Alliance and licensed to me photos I like. I am open to suggestions.
web address is carebrightpath.example
Call to schedule 855-555-0148
TCD is a safe and accurate tool that makes stroke prevention possible for your SCD patients and family.
Risk is highest for SCD sufferers age 2 to 5. Protect your childs future.

Target Market(s)

Parents, families and medical professionals

Industry/Entity Type

Medical wellness

Font styles to use
Other font styles liked:
• something close to my logo font

Colors
0094D4
00A9DD
6FCCEA
C7EBF8
E9F6FB

Requirements
Nice to have
• pictures of kids (Children of color) pictures of Brains, kids happy with medical professionals
Should not have
• dark colors

```html
<!DOCTYPE html>
<html lang="en">
<head>
<meta charset="utf-8">
<title>Sickle Cell Stroke Prevention Flyer</title>
<link rel="stylesheet" href="https://fonts.googleapis.com/css2?family=Mystery+Quest&family=Poppins:wght@400;500;600;700&display=swap">
<style>
  :root{
    --stage:#0e0d36;
    --navy:#164a85;
    --sky-pale:#e9f6fb;
    --sky-light:#c7ebf8;
    --sky-mid:#6fccea;
    --sky-card:#8fd8f0;
    --blue:#0094d4;
    --white:#ffffff;
    --display:"Mystery Quest", cursive;
    --body:"Poppins", sans-serif;
  }
  *{box-sizing:border-box;margin:0;padding:0}
  html,body{width:1200px;height:1200px;overflow:hidden;background:var(--stage)}
  .flyer{position:absolute;left:168px;top:45px;width:864px;height:1110px;background:var(--sky-pale);overflow:hidden;font-family:var(--body);color:var(--navy)}
  .hero{position:absolute;left:0;top:0;width:864px;height:466px;background:var(--sky-pale)}
  .brand{position:absolute;left:26px;top:70px;display:flex;align-items:center;gap:12px}
  .brand-mark{width:30px;height:30px;background:var(--blue)}
  .brand-name{font-family:var(--body);font-weight:600;font-size:30px;color:var(--navy);line-height:1}
  .headline{position:absolute;left:26px;top:224px;width:350px;font-family:var(--display);font-size:35px;line-height:38px;color:var(--navy)}
  .intro{position:absolute;left:26px;top:388px;width:370px;font-size:17px;line-height:23.5px;color:var(--navy)}
  .hero-photo{position:absolute;left:400px;top:14px;width:455px;height:452px;background:radial-gradient(ellipse at 45% 40%, #ffffff 0%, #dff1f9 55%, #cde7f3 100%)}
  .divider{position:absolute;left:0;top:466px;width:864px;height:13px;background:var(--white)}
  .info{position:absolute;left:0;top:479px;width:864px;height:485px;background:var(--sky-mid)}
  .pill{position:absolute;left:50%;transform:translateX(-50%);background:var(--navy);color:var(--white);font-family:var(--display);font-size:25px;line-height:32px;border-radius:8px;white-space:nowrap;width:170px;text-align:center}
  .pill-features{top:12px}
  .pill-facts{top:148px}
  .feature{position:absolute;top:55px;width:345px;height:71px;background:var(--sky-card);border-radius:8px;display:flex;align-items:center;padding-left:15px}
  .feature-a{left:66px}
  .feature-b{left:450px}
  .feature .icon{width:54px;height:54px;flex:none}
  .feature .rule{width:2px;height:44px;background:var(--navy);margin:0 12px;flex:none}
  .feature p{font-size:15px;line-height:19px;color:var(--white);font-weight:500}
  .facts-col{position:absolute;top:192px;width:380px;display:flex;flex-direction:column}
  .facts-left{left:38px;gap:16px}
  .facts-right{left:450px;gap:12px}
  .fact{display:flex;align-items:center;gap:20px}
  .fact .icon{width:46px;height:46px;flex:none}
  .fact p{width:312px;font-size:13.5px;line-height:17.5px;color:var(--white);font-weight:500;text-align:justify;text-align-last:left}
  .lower{position:absolute;left:0;top:964px;width:864px;height:89px;background:var(--sky-light)}
  .callout{position:absolute;left:80px;top:938px;width:701px;height:55px;background:var(--white);border:1px solid var(--navy);border-radius:8px;text-align:center;padding-top:4px}
  .callout strong{display:block;font-size:16px;line-height:22px;font-weight:600;color:var(--navy)}
  .callout span{display:block;font-size:15.5px;line-height:22px;color:var(--navy)}
  .tagline{position:absolute;left:0;top:1001px;width:864px;text-align:center;font-family:var(--display);font-size:36px;line-height:44px;color:var(--navy)}
  .tagline .star{display:inline-block;vertical-align:middle;margin:0 18px}
  .footer{position:absolute;left:0;top:1053px;width:864px;height:57px}
  .footer svg{position:absolute;left:0;top:0}
  .footer-web{position:absolute;left:59px;top:15px;font-size:15px;color:var(--white)}
  .footer-web b{font-weight:700}
  .footer-call{position:absolute;left:460px;top:8px;font-size:15px;color:var(--white)}
  .footer-call b{font-size:24px;font-weight:700;letter-spacing:0.5px;vertical-align:-2px}
</style>
</head>
<body>
<main class="flyer">
  <section class="hero">
    <div class="brand"><span class="brand-mark"></span><span class="brand-name">CareBright Path</span></div>
    <h1 class="headline">Stroke Prevention for Children with Children with Sickle Cell Disease is Possible!</h1>
    <p class="intro">TCD is a safe and accurate tool that makes stroke prevention possible for your SCD patients and family</p>
    <div class="hero-photo" role="img" aria-label="Photo of a smiling doctor in a white coat giving a thumbs up beside a young girl, over a faint brain outline"></div>
  </section>
  <div class="divider"></div>

  <section class="info">
    <div class="pill pill-features">Key Features</div>
    <div class="feature feature-a">
      <svg class="icon" viewBox="0 0 54 54"><circle cx="27" cy="27" r="25" fill="#fff" stroke="#164a85" stroke-width="3"/><circle cx="27" cy="27" r="17" fill="none" stroke="#164a85" stroke-width="2.5"/><line x1="15" y1="39" x2="39" y2="15" stroke="#164a85" stroke-width="2.5"/><path d="M22 22a7 7 0 0 0 0 10M32 22a7 7 0 0 1 0 10" fill="none" stroke="#164a85" stroke-width="2"/></svg>
      <span class="rule"></span>
      <p>Simple and painless screening<br>for your child</p>
    </div>
    <div class="feature feature-b">
      <svg class="icon" viewBox="0 0 54 54"><circle cx="27" cy="27" r="25" fill="#fff" stroke="#164a85" stroke-width="3"/><path d="M20 22h8l-1 12h-6z" fill="none" stroke="#164a85" stroke-width="2"/><path d="M24 34v4c0 3 3 4 6 4h8" fill="none" stroke="#164a85" stroke-width="2"/><path d="M19 17a8 8 0 0 1 10 0M21 14a12 12 0 0 1 6 0" fill="none" stroke="#164a85" stroke-width="1.8"/></svg>
      <span class="rule"></span>
      <p>Our Screening uses ultrasound<br>which is transcranial doppler</p>
    </div>

    <div class="pill pill-facts">Key Facts</div>

    <div class="facts-col facts-left">
      <div class="fact">
        <svg class="icon" viewBox="0 0 46 46"><circle cx="23" cy="23" r="21" fill="#e9f6fb" stroke="#fff" stroke-width="3"/><circle cx="23" cy="23" r="15" fill="none" stroke="#164a85" stroke-width="2"/><circle cx="19" cy="19" r="2.5" fill="#164a85"/><circle cx="25" cy="24" r="2.5" fill="#164a85"/><circle cx="19" cy="28" r="2.5" fill="#164a85"/><circle cx="27" cy="17" r="2" fill="#164a85"/></svg>
        <p>Sickle cell disease (SCD) is a blood disorder in which misshapen or “sickled” red blood cells can clog blood vessels and cause complications such as stroke and blood vessel damage</p>
      </div>
      <div class="fact">
        <svg class="icon" viewBox="0 0 46 46"><circle cx="23" cy="23" r="21" fill="#e9f6fb" stroke="#fff" stroke-width="3"/><path d="M17 12c0 8 12 14 12 22M29 12c0 8-12 14-12 22" fill="none" stroke="#164a85" stroke-width="2"/></svg>
        <p>The most severe form of the disease, called sickle cell anemia, occurs when a person inherits two abnormal copies of the hemoglobin-Beta gene</p>
      </div>
      <div class="fact">
        <svg class="icon" viewBox="0 0 46 46"><circle cx="23" cy="23" r="21" fill="#e9f6fb" stroke="#fff" stroke-width="3"/><ellipse cx="22" cy="22" rx="11" ry="9" fill="none" stroke="#164a85" stroke-width="2"/><line x1="22" y1="13" x2="22" y2="31" stroke="#164a85" stroke-width="1.5"/><circle cx="31" cy="30" r="5" fill="#0094d4"/></svg>
        <p>Stroke risk increases over 100-fold in children with SCD compared to children without sickle cell disease</p>
      </div>
    </div>

    <div class="facts-col facts-right">
      <div class="fact">
        <svg class="icon" viewBox="0 0 46 46"><circle cx="23" cy="23" r="21" fill="#e9f6fb" stroke="#fff" stroke-width="3"/><circle cx="23" cy="17" r="6" fill="none" stroke="#164a85" stroke-width="2"/><path d="M15 35c0-7 3-11 8-11s8 4 8 11z" fill="none" stroke="#164a85" stroke-width="2"/></svg>
        <p>All babies in the U.S. are screened for sickle cell disease, which affects 1 in 2,400 children, and 1 in 400 Black children</p>
      </div>
      <div class="fact">
        <svg class="icon" viewBox="0 0 46 46"><circle cx="23" cy="23" r="21" fill="#e9f6fb" stroke="#fff" stroke-width="3"/><text x="23" y="28" text-anchor="middle" font-family="Mystery Quest, cursive" font-size="16" fill="#164a85">11%</text></svg>
        <p>About 11% of SCD patients have strokes before age 20 with the highest risk between age 2 and 5</p>
      </div>
      <div class="fact">
        <svg class="icon" viewBox="0 0 46 46"><circle cx="23" cy="23" r="21" fill="#e9f6fb" stroke="#fff" stroke-width="3"/><rect x="12" y="15" width="20" height="14" rx="5" fill="none" stroke="#164a85" stroke-width="2"/><circle cx="31" cy="29" r="5" fill="#164a85"/><path d="M29 27l4 4M33 27l-4 4" stroke="#fff" stroke-width="1.3"/></svg>
        <p>The common stroke in children with sickle cell disease is “silent strokes,” or “silent” injury to the brain.</p>
      </div>
      <div class="fact">
        <svg class="icon" viewBox="0 0 46 46"><circle cx="23" cy="23" r="21" fill="#e9f6fb" stroke="#fff" stroke-width="3"/><path d="M16 34v-8c-3-2-3-9 3-11 5-2 11 1 11 7v3l3 2-3 1v6z" fill="none" stroke="#164a85" stroke-width="2"/><path d="M23 11l-2 5h3l-2 5" fill="none" stroke="#0094d4" stroke-width="1.6"/></svg>
        <p>There are two main types of strokes: Ischemicand hemorrhagic. Ischemic strokes are more common in children</p>
      </div>
    </div>
  </section>

  <div class="lower"></div>
  <div class="callout">
    <strong>Screening or early signs of stroke</strong>
    <span>can be a tool to for early diagnosis allowing for treatments that eliminate the risk</span>
  </div>
  <p class="tagline">
    <svg class="star" width="20" height="20" viewBox="0 0 20 20"><path d="M10 1l2.6 6 6.4.5-4.9 4.2 1.5 6.3L10 14.6 4.4 18l1.5-6.3L1 7.5 7.4 7z" fill="#fff"/></svg>Protect your childs future<svg class="star" width="20" height="20" viewBox="0 0 20 20"><path d="M10 1l2.6 6 6.4.5-4.9 4.2 1.5 6.3L10 14.6 4.4 18l1.5-6.3L1 7.5 7.4 7z" fill="#fff"/></svg>
  </p>

  <footer class="footer">
    <svg width="864" height="57" viewBox="0 0 864 57">
      <defs><linearGradient id="footerFade" x1="0" y1="0" x2="1" y2="0"><stop offset="0" stop-color="#5aa5db"/><stop offset="1" stop-color="#7bbde6"/></linearGradient></defs>
      <rect x="0" y="10" width="864" height="47" fill="url(#footerFade)"/>
      <path d="M387 0H864V57H347Z" fill="#164a85"/>
    </svg>
    <p class="footer-web">Visit: <b>www.carebrightpath.example</b></p>
    <p class="footer-call">Call to schedule: <b>855-555-0148</b></p>
  </footer>
</main>
</body>
</html>
```